U.S. based testing, inspection, and certification (TIC) company needs a new PowerPoint template.

We need a new PowerPoint template (deck, slide deck) for our U.S. based company with international capabilities for performing numerous testing, inspection, and certification (TIC) services. Our primary services include calibration, chemical analysis, consulting engineering, environmental simulation, forensic engineering, materials testing, mechanical testing, and nondestructive testing. Industries we serve are aerospace/aviation, automotive, chemical, commercial properties, construction, consumer products, defense, energy storage, healthcare, insurance/legal, life science, manufacturing, oil & gas, power generation, pulp & paper, and telecommunications. https://qorvenlab.com/

Guideline hex colors: #29aae2, #0b1f3b, #fb6805 (use orange more subtly)

The final design should communicate:
1. Trust, Integrity, and Independence
2. Technical Expertise and Accuracy
3. Efficiency and Speed
4. Value-Added Partnership

Our current branding reflects a variety of styles, several of which have been included as attachments for reference in this project. While these examples showcase the direction we have taken in the past, we are not limited to them and remain open to exploring fresh, innovative design that is simple, clean, and with plenty of space to add content for each slide. We welcome creative concepts that build on or reimagine our existing identity to better align with our evolving vision.

```html
<!DOCTYPE html>
<html lang="en">
<head>
<meta charset="utf-8">
<title>Qorven Technical Services – Deck Overview</title>
<link href="https://fonts.googleapis.com/css2?family=Inter:wght@400;500;600;700;800&display=swap" rel="stylesheet">
<style>
:root{
  --page:#ffffff;
  --board:#0d2a57;
  --slide:#143e82;
  --slide-deep:#0f336e;
  --bar:#4b74b1;
  --pill:#3f68a8;
  --pill-dark:#0b2552;
  --card:#2a5597;
  --orange:#fb6805;
  --white:#ffffff;
  --soft:#c9d6ee;
  --sky:#29aae2;
}
*{margin:0;padding:0;box-sizing:border-box}
html,body{width:1200px;height:567px;overflow:hidden;background:var(--page);font-family:'Inter',sans-serif;color:var(--white)}
.section-tag{position:absolute;left:14px;top:1.5px;height:10px;padding:0 3px;background:var(--board);border-radius:1.5px;font-size:4px;line-height:10px;color:var(--white);white-space:nowrap}
.board{position:absolute;left:14px;top:14px;width:1172px;height:538px;background:var(--board)}
.slide{position:absolute;width:272px;height:152px;overflow:hidden;background:var(--slide)}
.c1{left:48.5px}.c2{left:325.5px}.c3{left:602.5px}.c4{left:879.5px}
.r1{top:48.5px}.r2{top:207px}.r3{top:365px}
.abs{position:absolute}
.bar{position:absolute;left:15px;top:12.5px;width:241px;height:16.5px;background:var(--bar);border-right:3.7px solid var(--orange);font-size:7px;font-weight:700;line-height:16.5px;padding-left:5.5px}
.hero-bg{background:linear-gradient(125deg,#1b4db8 0%,#4d74d6 28%,#b9c3ea 48%,#7d97dc 62%,#2453c4 80%,#1743b0 100%)}
.brand{font-weight:700;color:var(--white);display:flex;align-items:center;gap:2px}
.brand i{display:block;width:4px;height:4px;background:var(--white)}
.orange{color:var(--orange)}
.tiny{font-size:2.6px;line-height:3.4px;color:var(--soft)}
.toc-num{position:absolute;font-size:6px;font-weight:700}
.toc-lbl{position:absolute;font-size:6px}
.photo{position:absolute;background:linear-gradient(135deg,#e9eef1 0%,#b8c3c7 45%,#5f8a86 70%,#dfe5e8 100%)}
.map{position:absolute;background:radial-gradient(ellipse at 40% 60%,#2f5da0 0%,#1d4a8c 55%,rgba(20,62,130,0) 80%)}
.tag{position:absolute;left:172px;width:80px;height:14px;background:var(--slide-deep);border-left:2.5px solid var(--orange);font-size:3.3px;line-height:14px;padding-left:12px;white-space:nowrap}
.pill{position:absolute;height:12px;background:var(--pill);font-size:4px;line-height:12px;text-align:center;white-space:nowrap}
.pill.hot{background:var(--orange)}
.pill.dark{background:var(--pill-dark)}
.card{position:absolute;width:98px;height:33.5px;background:var(--card);padding:3px 3.5px;overflow:hidden}
.card .ico{width:8.5px;height:8.5px;border-radius:50%;background:var(--orange);display:flex;align-items:center;justify-content:center}
.card .ico span{width:3px;height:3px;border:0.6px solid var(--white);border-radius:50%}
.card h4{font-size:5px;font-weight:500;margin-top:2.5px;line-height:6px}
.card p{font-size:2.5px;line-height:3px;color:var(--soft)}
.step{position:absolute;top:68.5px;width:9px;height:9px;border-radius:50%;background:var(--white);color:#0b1f3b;font-size:4px;font-weight:700;text-align:center;line-height:9px;margin-left:-4.5px}
.step-lbl{position:absolute;top:82.5px;width:40px;margin-left:-20px;text-align:center;font-size:3.8px;line-height:5px}
.lead{font-size:6px;line-height:8px}
.driver{position:absolute;left:152px;width:110px;display:flex;gap:4px;font-size:3.3px;line-height:4px;color:var(--soft)}
.driver svg{flex:none}
.member{position:absolute;top:55px;width:39px}
.member .face{width:39px;height:38.5px;background:linear-gradient(160deg,#d8d1c6,#a88f77 55%,#6d4f3a)}
.member b{display:block;font-size:4.8px;font-weight:400;margin-top:6px}
.member small{display:block;font-size:3.4px;color:var(--soft)}
.cred{position:absolute;top:81px;width:72px}
.cred h5{font-size:6px;font-weight:400;line-height:5.8px;padding-left:11px;position:relative}
.cred h5 i{position:absolute;left:0;top:0;width:7px;height:7px;border:0.7px solid var(--soft);border-radius:1px}
.cred p{font-size:2.8px;line-height:3.3px;color:var(--soft);padding-left:11px;margin-top:3px}
</style>
</head>
<body>
<div class="section-tag">Section 2</div>
<div class="board"></div>

<!-- Cover -->
<section class="slide c1 r1 hero-bg">
  <div class="abs" style="left:22px;top:27px;font-size:2.8px;background:#0b1f3b;padding:0.6px 2px;white-space:nowrap">GLOBAL TIC LEADER</div>
  <div class="abs brand" style="left:0;width:272px;justify-content:center;top:28px;font-size:6px"><i></i>QORVEN</div>
  <h1 class="abs" style="left:0;width:272px;top:57px;text-align:center;font-size:14.5px;line-height:14.5px;font-weight:800">QORVEN TECHNICAL<br>SERVICES</h1>
  <div class="abs" style="left:57px;top:91px;width:161px;height:0.8px;background:var(--orange)"></div>
  <p class="abs" style="left:60px;top:97px;width:155px;text-align:center;font-size:3.6px;line-height:3.6px">Engineering confidence across borders — delivering precision, compliance, and trust to the world's most demanding industries.</p>
</section>

<!-- Contents -->
<section class="slide c2 r1">
  <div class="bar">Table of Contents</div>
  <span class="toc-num" style="left:21px;top:51px">1</span><span class="toc-lbl" style="left:43px;top:51px">About Us</span>
  <span class="toc-num" style="left:21px;top:64.5px">2</span><span class="toc-lbl" style="left:43px;top:64.5px">Industry Challenges</span>
  <span class="toc-num" style="left:21px;top:79.5px">3</span><span class="toc-lbl" style="left:43px;top:79.5px">Our Capabilities</span>
  <span class="toc-num" style="left:21px;top:95.5px">4</span><span class="toc-lbl" style="left:43px;top:95.5px">Industries Served</span>
  <span class="toc-num" style="left:21px;top:111.5px">5</span><span class="toc-lbl" style="left:43px;top:111.5px">Our Process</span>
  <span class="toc-num" style="left:136px;top:51px">6</span><span class="toc-lbl" style="left:158px;top:51px">Why Choose Us</span>
  <span class="toc-num" style="left:136px;top:64.5px">7</span><span class="toc-lbl" style="left:158px;top:64.5px">Key Insights</span>
  <span class="toc-num" style="left:136px;top:79.5px">8</span><span class="toc-lbl" style="left:158px;top:79.5px">Meet the team</span>
  <span class="toc-num" style="left:136px;top:95.5px">9</span><span class="toc-lbl" style="left:158px;top:95.5px">Global Reach</span>
  <span class="toc-num" style="left:136px;top:111.5px">10</span><span class="toc-lbl" style="left:158px;top:111.5px">Contact</span>
</section>

<!-- About -->
<section class="slide c3 r1">
  <div class="bar">About Us</div>
  <p class="abs lead" style="left:21px;top:56px">Independent Expertise.<br><span class="orange">Trusted</span> Results.</p>
  <p class="abs tiny" style="left:21px;top:79.5px;width:88px">For more than three decades, we have helped organizations make informed decisions through reliable testing, inspection, and certification services. Our multidisciplinary teams combine technical expertise with advanced laboratory capabilities to deliver accurate, unbiased results that support safety, compliance, and performance across a wide range of industries.</p>
  <div class="photo" role="img" aria-label="Gloved hands examining a component with a magnifying glass" style="left:135.5px;top:44px;width:110.5px;height:78px"></div>
  <div class="abs" style="left:246px;top:44px;width:10px;height:78px;background:var(--slide-deep)"></div>
</section>

<!-- Challenges -->
<section class="slide c4 r1">
  <div class="bar">Industry Challenges</div>
  <div class="map" role="img" aria-label="World map outline" style="left:0;top:70px;width:200px;height:82px"></div>
  <p class="abs" style="left:0;width:272px;top:37.5px;text-align:center;font-size:6px;line-height:8.3px">Meeting <span class="orange">Higher Standards</span> in a<br>Complex World</p>
  <p class="abs tiny" style="left:84px;top:58px;width:104px;text-align:center;font-size:2.5px;line-height:3.1px">Today's industries operate in an environment of increasing regulatory requirements, accelerated product development cycles, and growing expectations for safety and reliability. Organizations need trusted technical partners who can provide accurate data, reduce risk, and help maintain compliance without slowing innovation.</p>
  <div class="tag" style="top:90px">TRUSTED PARTNERS</div>
  <div class="tag" style="top:109.5px">REGULATORY REQUIREMENTS</div>
  <div class="tag" style="top:129px">RISK REDUCTION</div>
</section>

<!-- Capabilities -->
<section class="slide c1 r2">
  <div class="bar">Our Capabilities</div>
  <div class="pill" style="left:67px;top:42px;width:71px">Calibration</div>
  <div class="pill" style="left:141px;top:42px;width:71px">Chemical Analysis</div>
  <div class="pill hot" style="left:54px;top:58px;width:84px">Consulting Engineering</div>
  <div class="pill dark" style="left:141px;top:58px;width:86px">Environmental Simulation</div>
  <div class="pill dark" style="left:35px;top:73px;width:103px">Forensic Engineering</div>
  <div class="pill" style="left:141px;top:73px;width:101px">Materials Testing</div>
  <div class="pill" style="left:67px;top:87.5px;width:71px">Mechanical Testing</div>
  <div class="pill hot" style="left:141px;top:87.5px;width:71px">Non-Destructive Testing</div>
  <p class="abs" style="left:80px;top:121.5px;width:112px;text-align:center;font-size:3px;line-height:3.8px">Comprehensive solutions designed to support product quality, operational reliability, and regulatory compliance.</p>
</section>

<!-- Industries -->
<section class="slide c2 r2">
  <div class="bar">Industries Served</div>
  <div class="card" style="left:36px;top:37px"><div class="ico"><span></span></div><h4>Oil, Gas &amp; Energy</h4><p>Pipeline inspection, offshore certification, pressure vessel testing, and process safety audits under API, ASME, and ISO standards.</p></div>
  <div class="card" style="left:137px;top:37px"><div class="ico"><span></span></div><h4>Aerospace &amp; Defense</h4><p>Structural integrity testing, NDT, AS9100 quality system certification, and material qualification for flight-critical components.</p></div>
  <div class="card" style="left:36px;top:73px"><div class="ico"><span></span></div><h4>Automotive &amp; EV</h4><p>Safety inspection, battery system certification, EMC testing, and type-approval services for conventional and electric vehicle platforms.</p></div>
  <div class="card" style="left:137px;top:73px"><div class="ico"><span></span></div><h4>Healthcare &amp; Life Sciences</h4><p>Biocompatibility testing, medical device verification, GMP audits, and regulatory compliance under FDA, MDR/IVDR, and WHO frameworks.</p></div>
  <div class="card" style="left:36px;top:109.5px"><div class="ico"><span></span></div><h4>Construction &amp; Infrastructure</h4><p>Structural inspection, geotechnical testing, fire safety certification, and environmental compliance for civil and industrial projects.</p></div>
  <div class="card" style="left:137px;top:109.5px"><div class="ico"><span></span></div><h4>Food &amp; Agriculture</h4><p>HACCP audits, ISO 22000 certification, pesticide residue testing, and supply chain traceability for global food safety compliance.</p></div>
</section>

<!-- Process -->
<section class="slide c3 r2">
  <div class="abs" style="left:54px;top:0;width:54.5px;height:152px;background:#123a7b"></div>
  <div class="abs" style="left:108.5px;top:0;width:54.5px;height:152px;background:#103672"></div>
  <div class="abs" style="left:163px;top:0;width:54.5px;height:152px;background:#0e3169"></div>
  <div class="abs" style="left:217.5px;top:0;width:54.5px;height:152px;background:#0c2c60"></div>
  <div class="bar">Our Process</div>
  <p class="abs" style="left:21px;top:42px;font-size:3.8px">A structured, data-driven process:</p>
  <div class="abs" style="left:30px;top:72.8px;width:214px;height:0.5px;background:var(--soft)"></div>
  <div class="step" style="left:30px">1</div><div class="step-lbl" style="left:30px">Scope Definition</div>
  <div class="step" style="left:81px">2</div><div class="step-lbl" style="left:83px">Testing Execution</div>
  <div class="step" style="left:135.5px">3</div><div class="step-lbl" style="left:135.5px">Data Analysis</div>
  <div class="step" style="left:189.6px">4</div><div class="step-lbl" style="left:189.6px">Validation</div>
  <div class="step" style="left:244px;outline:0.8px dashed var(--orange);outline-offset:1px">5</div><div class="step-lbl" style="left:243px">Certification &amp;<br>Reporting</div>
  <div class="abs" role="img" aria-label="Faint gears and rising arrow motif" style="left:0;top:108px;width:70px;height:44px;background:radial-gradient(ellipse at 40% 70%,rgba(75,116,177,0.45),rgba(20,62,130,0) 70%)"></div>
</section>

<!-- Why -->
<section class="slide c4 r2" style="background:linear-gradient(170deg,#1c4fb8 0%,#7d95dc 25%,#2a58bf 40%,var(--slide) 42%,var(--slide) 100%)">
  <div class="bar">Why Choose Us</div>
  <p class="abs lead" style="left:18px;top:78px">Delivering <span class="orange">More</span> Than Test<br>Results</p>
  <p class="abs tiny" style="left:18px;top:101.5px;width:92px;font-size:2.6px;line-height:3.1px">Our clients value our commitment to independence, technical excellence, and responsive service. By combining advanced capabilities with industry knowledge, we help organizations improve decision-making, reduce risk, and achieve their operational objectives more efficiently.</p>
  <div class="photo" role="img" aria-label="Gloved hands examining a component with a magnifying glass" style="left:133px;top:65px;width:111px;height:78px"></div>
  <div class="abs" style="left:244px;top:65px;width:10px;height:78px;background:var(--slide-deep)"></div>
</section>

<!-- Insights -->
<section class="slide c1 r3">
  <div class="bar">Key Insights</div>
  <div class="abs" style="left:15px;top:38px;width:33px;height:4.5px;border-radius:3px;background:var(--pill);font-size:2.2px;line-height:4.5px;text-align:center;white-space:nowrap">Market Size (USD Bn)</div>
  <div class="abs" style="left:51px;top:38px;width:16px;height:4.5px;border-radius:3px;background:var(--pill);font-size:2.2px;line-height:4.5px;text-align:center">CAGR %</div>
  <svg class="abs" style="left:12px;top:44px" width="136" height="86" viewBox="0 0 136 86" font-family="Inter, sans-serif" font-size="2.2" fill="#c9d6ee">
    <line x1="10" y1="8" x2="10" y2="68" stroke="#6f8fc4" stroke-width="0.4"/>
    <line x1="10" y1="68" x2="129" y2="68" stroke="#6f8fc4" stroke-width="0.4"/>
    <text x="3" y="13.5">400</text><text x="3" y="27.5">300</text><text x="3" y="41.5">200</text><text x="3" y="55.5">100</text><text x="6" y="69">0</text>
    <text x="119" y="4">CAGR %</text><text x="131" y="39">4</text><text x="131" y="58">2</text><text x="131" y="69">0</text>
    <g fill="#2f7df2">
      <rect x="12.7" y="32" width="14.4" height="36"/>
      <rect x="32.3" y="30" width="14.4" height="38"/>
      <rect x="52.3" y="26" width="14.4" height="42"/>
      <rect x="71.8" y="21.4" width="14.4" height="46.6"/>
      <rect x="91.8" y="16.3" width="14.4" height="51.7"/>
      <rect x="111.3" y="9" width="14.4" height="59"/>
    </g>
    <path d="M18 68 C22 30 26 10 36 8 C50 6 80 8 125 8" fill="none" stroke="#29aae2" stroke-width="0.6"/>
    <text x="17" y="73">2024</text><text x="36.5" y="73">2025</text><text x="56.5" y="73">2027</text><text x="76" y="73">2029</text><text x="96" y="73">2031</text><text x="115.5" y="73">2034</text>
    <text x="64" y="80">Year</text>
  </svg>
  <p class="abs" style="left:15px;top:130px;width:128px;font-size:3.3px;line-height:4px">Global TIC market projected to reach <b>USD 430.3 billion by 2034</b>, growing at a CAGR of 5.2%. Source: Global Sector Research, 2025.</p>
  <p class="abs" style="left:153px;top:43px;font-size:5px">Key Growth Drivers</p>
  <div class="driver" style="top:51px"><svg width="7" height="5" viewBox="0 0 7 5"><path d="M0 2.5H6M4 0.5L6 2.5 4 4.5" stroke="#29aae2" stroke-width="0.5" fill="none"/></svg><span>Stricter product safety and regulatory mandates across 120+ countries</span></div>
  <div class="driver" style="top:69px"><svg width="7" height="5" viewBox="0 0 7 5"><path d="M0 2.5H6M4 0.5L6 2.5 4 4.5" stroke="#29aae2" stroke-width="0.5" fill="none"/></svg><span>Rapid expansion of EV, renewable energy, and green technology sectors</span></div>
  <div class="driver" style="top:86.5px"><svg width="7" height="5" viewBox="0 0 7 5"><path d="M0 2.5H6M4 0.5L6 2.5 4 4.5" stroke="#29aae2" stroke-width="0.5" fill="none"/></svg><span>Rising demand for ESG compliance and sustainability certification</span></div>
  <div class="driver" style="top:104.5px"><svg width="7" height="5" viewBox="0 0 7 5"><path d="M0 2.5H6M4 0.5L6 2.5 4 4.5" stroke="#29aae2" stroke-width="0.5" fill="none"/></svg><span>Adoption of AI, IoT, and digital inspection platforms by TIC providers</span></div>
  <div class="driver" style="top:122px"><svg width="7" height="5" viewBox="0 0 7 5"><path d="M0 2.5H6M4 0.5L6 2.5 4 4.5" stroke="#29aae2" stroke-width="0.5" fill="none"/></svg><span>Globalization of supply chains increasing cross-border conformity requirements</span></div>
</section>

<!-- Team -->
<section class="slide c2 r3">
  <div class="bar">Meet The Team</div>
  <div class="member" style="left:42.5px"><div class="face" role="img" aria-label="Portrait of team member Dylan Rook"></div><b>Dylan Rook</b><small>Position</small></div>
  <div class="member" style="left:108px"><div class="face" role="img" aria-label="Portrait of team member Mara Vell"></div><b>Mara Vell</b><small>Position</small></div>
  <div class="member" style="left:173.5px"><div class="face" role="img" aria-label="Portrait of team member Theo Lark"></div><b>Theo Lark</b><small>Position</small></div>
</section>

<!-- Reach -->
<section class="slide c3 r3">
  <div class="bar">Global Reach</div>
  <h2 class="abs" style="left:21px;top:47px;font-size:10.3px;font-weight:400;white-space:nowrap">Internationally Recognized Credentials</h2>
  <p class="abs" style="left:21px;top:61px;width:200px;font-size:3px;line-height:3.6px;color:var(--soft)">Our accreditations are not checkboxes — they represent independently verified technical competence, impartiality, and system integrity, recognized by regulators and buyers in every major market.</p>
  <div class="cred" style="left:21px"><h5><i></i>ISO/IEC 17025 —<br>Laboratory<br>Competence</h5><p>Accreditation of our testing and calibration laboratories, confirming technical capability, measurement traceability, and impartiality of results under national accreditation bodies worldwide.</p></div>
  <div class="cred" style="left:98.5px"><h5><i></i>ISO/IEC 17065 —<br>Product Certification<br>Bodies</h5><p>Formal accreditation to operate as a third-party product certification body, enabling us to issue marks recognized for regulatory compliance, trade facilitation, and consumer protection across 120+ countries.</p></div>
  <div class="cred" style="left:176px"><h5><i></i>ISO/IEC 17020 —<br>Inspection Bodies</h5><p>Accreditation of our inspection activities confirming independence, defined processes, and technical integrity in all physical and remote inspection engagements across energy, marine, construction, and manufacturing sectors.</p></div>
</section>

<!-- Thanks -->
<section class="slide c4 r3 hero-bg">
  <div class="abs brand" style="left:0;width:272px;justify-content:center;top:30px;font-size:6px"><i></i>QORVEN</div>
  <h2 class="abs" style="left:0;width:272px;top:69px;text-align:center;font-size:12px;font-weight:800">THANK YOU</h2>
  <p class="abs" style="left:15.5px;top:104.5px;font-size:4.8px">Get in touch with us!</p>
  <p class="abs" style="left:15.5px;top:118px;font-size:4.8px;line-height:6.8px">@qorvenlab<br>hello@qorvenlab.com<br>www.qorvenlab.com</p>
</section>
</body>
</html>
```